RT Appraisals website redesign

I would like to refresh my existing website of www.rtappraisals.example with new graphics, look and feel, as well as updated structure and wording. Content and layout changes have been uploaded to this project Brief.

My existing website has a dark feel. I am now looking for a light and energetic feel. Financial Services is my industry, so the website should be reflect that. I would also like to reflect the concepts of Trust, Service and Expertise.

The website must be serious and upmarket.

Target Market(s)

Corporate board members, CFO's, treasurers and controllers
Auditors, tax advisors, private equity and venture capital asset managers, investors, tax authorities

Industry/Entity Type

Financial Service

Coding

Coded - Design and coding required

Number of Pages Required

5+ page

Font styles to use
Sans Serif
Other font styles liked:
• Designer can choose another modern font

Colors
0355a3
3277b5
85acd3
eaf1f7
f37122
f68d4d
9bcb3c
acd037
cadf82

Requirements
Must have
• Good hi resolution pictures that convey "Finance", "Trust", "Service" or "Expertise".
• An anti-bot (such as Captcha) mechanism in the contact form.
Should not have
• Must not have all content on one rolling screen.

```html
<!DOCTYPE html>
<html lang="en">
<head>
<meta charset="utf-8">
<title>News &amp; Views – RT Appraisals</title>
<link rel="stylesheet" href="https://fonts.googleapis.com/css2?family=Mulish:wght@400;600;700;800&display=swap">
<style>
:root{
  --blue:#0355a3;
  --orange:#f37122;
  --green:#9bcb3c;
  --ink:#2b2b2b;
  --text:#666;
  --grey-nav:#777;
  --card:#f2f2f2;
  --footer:#333333;
  --footer-line:#555;
  --footer-text:#999;
}
*{box-sizing:border-box;margin:0;padding:0}
html,body{width:1024px;height:1200px;overflow:hidden}
body{position:relative;font-family:"Mulish",sans-serif;background:#fff;color:var(--text)}
.site-header{position:absolute;left:0;top:0;width:1024px;height:85px;
  background:linear-gradient(90deg,#e2e2da 0%,#ecece2 40%,#f4f4e4 100%)}
.brand{position:absolute;left:138px;top:30px;font-weight:700;font-size:19px;letter-spacing:.5px;color:#8a8a8a}
.main-nav{position:absolute;right:138px;top:38px;display:flex;gap:35px}
.main-nav a,.footer-nav a{font-weight:700;font-size:10px;text-decoration:none;color:var(--grey-nav);letter-spacing:.2px}
.main-nav a.active{color:var(--blue)}
.page-title{position:absolute;top:157px;left:0;width:1024px;text-align:center;font-weight:800;font-size:33px;color:var(--orange);letter-spacing:.3px}
.news-grid{position:absolute;left:138px;top:223px;display:grid;grid-template-columns:repeat(3,230px);grid-auto-rows:176px;column-gap:29px;row-gap:29px}
.news-card{background:var(--card);padding:15px 11px}
.news-card.center{grid-column:2}
.news-card h2{font-weight:700;font-size:10.2px;line-height:16.6px;color:var(--ink)}
.news-card time{display:block;font-size:9.3px;line-height:16px;color:var(--blue);margin-bottom:17px}
.news-card p{font-size:9.5px;line-height:16.6px;color:var(--text)}
.news-card .more{display:inline-block;margin-top:4px;font-weight:700;font-size:10.5px;color:var(--green);text-decoration:none}
.site-footer{position:absolute;left:0;top:899px;width:1024px;height:301px}
.site-footer svg.bg{position:absolute;left:0;top:0}
.footer-brand{position:absolute;top:45px;left:0;width:1024px;text-align:center;font-weight:700;font-size:19px;letter-spacing:.5px;color:#8a8a8a}
.footer-nav{position:absolute;left:138px;top:124px;width:749px;height:38px;border-top:1px solid var(--footer-line);border-bottom:1px solid var(--footer-line);display:flex;justify-content:center;align-items:center;gap:34px}
.footer-nav a{color:#8a8a8a}
.footer-nav a.active{color:var(--green)}
.footer-col{position:absolute;top:184px}
.footer-col h3{font-weight:800;font-size:11px;color:var(--orange);margin-bottom:9px}
.footer-col p{font-size:9px;line-height:19px;color:var(--footer-text)}
.footer-col p b{font-weight:400;color:#eee}
.footer-col p em{font-style:normal;color:var(--green)}
.credits{left:139px}
.office{left:398px}
.contact-line{display:flex;align-items:flex-start;gap:8px;font-size:9px;color:var(--footer-text);line-height:14px}
.contact-line.phone{margin-top:10px;color:#fff;font-size:9.5px}
.badges{position:absolute;left:656px;top:209px;display:flex;gap:21px;align-items:center}
.badge{background:#555;border-radius:4px}
</style>
</head>
<body>
<header class="site-header">
  <div class="brand">RT APPRAISALS</div>
  <nav class="main-nav">
    <a href="#">HOME</a><a href="#">ABOUT</a><a href="#">SERVICES</a><a href="#" class="active">NEWS &amp; VIEWS</a><a href="#">CONTACT</a>
  </nav>
</header>

<h1 class="page-title">NEWS &amp; VIEWS</h1>

<main class="news-grid">
  <article class="news-card"><h2>Dutch GAAP Update – Goodwill and Definitions of Value</h2><time>March 9, 2016</time><p>A number of Dutch GAAP accounting changes took effect on January 1, 2016, some of which affect goodwill and definitions…</p><a class="more" href="#">READ MORE</a></article>
  <article class="news-card"><h2>Daniel Marsh to Speak at BridgeWest on Feb 18 in Elmstad, the Netherlands</h2><time>February 4, 2016</time><p>At $265 billion, the Netherlands is the 3rd largest foreign investor in the United States. The United States is the largest foreign…</p><a class="more" href="#">READ MORE</a></article>
  <article class="news-card"><h2>RT Appraisals presenteert bij BridgeWest op 18 februari in Elmstad</h2><time>February 4, 2016</time><p>Lakeside, 2 februari 2016 – Daniel Marsh, managing director van RT Appraisals, presenteert bij BridgeWest op 18 februari in…</p><a class="more" href="#">READ MORE</a></article>
  <article class="news-card"><h2>Northfield University Extends Financial Training Contract with RT Appraisals</h2><time>September 7, 2015</time><p>Lakeside, The Netherlands, September 7, 2015 – Northfield University has extended its contract with the financial training brand of…</p><a class="more" href="#">READ MORE</a></article>
  <article class="news-card"><h2>Hartley-Brooks Enters into Strategic Partnership with RT Appraisals</h2><time>July 21, 2015</time><p>Lakeside, The Netherlands, July 21, 2015 – RT Appraisals, a boutique valuation advisory practice headquartered in Lakeside, The…</p><a class="more" href="#">READ MORE</a></article>
  <article class="news-card"><h2>Standard of value for Dutch tax valuations</h2><time>December 04, 2018</time><p>To play the game you must know the rules. Take a simple deck of cards. There are fifty-two different cards in a standard…</p><a class="more" href="#">READ MORE</a></article>
  <article class="news-card center"><h2>The 4 Pillars of Business Valuation</h2><time>January 16, 2019</time><p>“Old ways do not always open new doors.” The field of business valuation is constantly changing and one cannot remain</p><a class="more" href="#">READ MORE</a></article>
</main>

<footer class="site-footer">
  <svg class="bg" width="1024" height="301" viewBox="0 0 1024 301"><polygon points="0,58 512,0 1024,58 1024,301 0,301" fill="#333333"/></svg>
  <div class="footer-brand">RT APPRAISALS</div>
  <nav class="footer-nav">
    <a href="#" class="active">HOME</a><a href="#">ABOUT</a><a href="#">SERVICES</a><a href="#">NEWS &amp; VIEWS</a><a href="#">CONTACT</a>
  </nav>
  <div class="footer-col credits">
    <h3>CREDITS</h3>
    <p>© 2019 <em>RT Appraisals B.V.</em></p>
    <p>Logo by <b>Mira Holt</b></p>
    <p>Website by <em>Clearline Studio</em></p>
  </div>
  <div class="footer-col office">
    <h3>LAKESIDE</h3>
    <div class="contact-line">
      <svg width="9" height="12" viewBox="0 0 9 12"><path d="M4.5 0C2 0 0 2 0 4.5 0 8 4.5 12 4.5 12S9 8 9 4.5C9 2 7 0 4.5 0zm0 6.3a1.8 1.8 0 1 1 0-3.6 1.8 1.8 0 0 1 0 3.6z" fill="#9bcb3c"/></svg>
      <span>Canal Street 48<br>1000 AB Lakeside</span>
    </div>
    <div class="contact-line phone">
      <svg width="11" height="11" viewBox="0 0 24 24"><path d="M6.6 10.8a15 15 0 0 0 6.6 6.6l2.2-2.2c.3-.3.7-.4 1-.2 1.1.4 2.3.6 3.6.6.6 0 1 .4 1 1V20c0 .6-.4 1-1 1C10.6 21 3 13.4 3 4c0-.6.4-1 1-1h3.5c.6 0 1 .4 1 1 0 1.3.2 2.5.6 3.6.1.3 0 .7-.2 1z" fill="#9bcb3c"/></svg>
      <span>010 555 0142</span>
    </div>
  </div>
  <div class="badges">
    <div class="badge" role="img" aria-label="Professional institute membership badge" style="width:102px;height:22px"></div>
    <div class="badge" role="img" aria-label="Appraisers society membership badge" style="width:104px;height:42px"></div>
  </div>
</footer>
</body>
</html>
```